Relaunch website sonnenundrhein.de

We are looking for creative minds to relaunch the website for our award-winning comedy musical “Wolken und Brise” (www.sonnenundrhein.de). The aim is a cheeky, funny and surprising website that underlines our position as “Germany's funniest musical” and motivates people to buy tickets. The site should convey the positive Cologne attitude to life, be responsive and offer intuitive navigation.

Design specifications: Magenta-purple as the main color with golden accents. Font: Bebas Neue for headlines, Open Sans Condensed for body text.
The heart logo is to be placed at the top left. Various key visuals such as a drawn Cologne skyline or other drawings etc. should be integrated.

In addition to the main page, the subpages: The Musical, Ticket Info, Plan a Visit, Company Events are to be created.

The winner will be selected according to the following criteria: Creativity, user guidance, technical feasibility and compliance with the style guide.

I have uploaded briefing documents in English If you have any questions, please contact lukas.brandt@veltora-buehne.

Further briefings and the style guide have been uploaded in the appendix.

Additionally, graphics can be downloaded under these links (the download of the files takes longer):

http://VELTORA-NAS.fernlager.example/d/s/12hIMn5Y8tBxruv0eqvaTYrfzCXX1ZXE/W2t9gugGTtFgGl2YAyfn0qzz0Jvma2EO-j7YglkhkKww

Link LOGO:
http://VELTORA-NAS.fernlager.example/d/s/12hzRrDEelalG3eIQ1zqq10t7HylrWfW/Y4BTw-kx2bB6SC1pgNFkVCuC0_7yzXY5-XLpAKylVKww

http://VELTORA-NAS.fernlager.example/d/s/12lNTwd0im1cftcjvYC45mULZ0Fh0YTU/rlBvu8wD4UG6w7gLlYP8xqw2kmzaoiy1-H7sAETBWKww

Target Market(s)

Germany-wide + region 40 kilometers around Cologne

Industry/Entity Type

Entertaunment Produktion

Coding

Coded - Design and coding required

Number of Pages Required

4 page

Font styles to use
Other font styles liked:
• Bebas Neue , Open Sans Condensed

Colors
E54698
E96AAD
F1A4CE
F9D9EA
FCEFF6
A7469A
B969AE
D3A5CF
EDDBEB
F8F0F9

Requirements
Must have
• Color scheme • Main color: magenta-violet • Accent color: gold/gold tones • Complementary colors: shades of the main color and neutral tones for body text Typography • Headlines: Bebas Neue (sans-serif, no italics or small capitals) • Copy texts: Open Sans Condensed (all styles allowed, no italics) • Clear hierarchy for optimal readability and recognition Logo • The heart logo must always appear on a heart-shaped background • Variants with the addition "The Cologne Musical" are possible • Prominent placement in all areas of the website Key visuals • Combination of striking illustrations with local Cologne symbols • Cologne skyline with cathedral and TV tower • Golden accents and rainbow elements • Kölsch glass as a local reference • Stylized graphic elements in gold (stars, glitter effects, frames) Website structure and content Header area • Dynamic news ticker with current offers and performance dates • Logo (left) and main navigation (right) • Prominently placed "Get Tickets" button in gold • Main menu items: Musical, Ticket Info, Plan Visit, Groups, Corporate Events, FAQ Hero Section • Emotionally effective video background or changing key visuals • Concise headline: "WOLKEN UND BRISE - The award-winning Cologne musical" • Subheadline with a special humorous component • Eye-catching CTA button "GET TICKETS" with price information Celebrity Endorsement Section • Creative slider concept with testimonials from well-known personalities • Integration of quotes from Marlene Oswitz, Reinhard Plomberg, Dieter Hanslik • Authentic representation of the celebrities in connection with the musical Awards & Headlines • Visual highlighting of the awards • Infographic on visitor numbers (144. 000+) and recommendation rate • Integration of the four German musical and theater awards as badges/icons Show description • Humorous presentation of the plot surrounding Pastor Gunnar • Creative visualization of the show highlights • List of special features (live orchestra, choreography, etc. ) • Integration of Cologne local flavor Press reviews slider • Dynamic concept for presenting press reviews • Integration of quotes from Blatt zum Montag, Kurier, Rheinische Morgenpost • Visual linking with the respective media logos Highlight scenes • Interactive photo gallery with short, witty descriptions • Potential integration of short video snippets • "Appetizers" without giving too much away about the musical USP section • Four concise icons with accompanying text • Highlighting the unique selling points: live orchestra, unique venue, sustainability, Cologne culture • Creative implementation of the icons in the style of the musical Voucher banner • Eye-catching design for the voucher area • Emotional appeal: "Give the gift of unforgettable moments" • Direct CTA for voucher ordering Visitor comments • Authentic testimonials with real visitor photos • Representation of various target group representatives • Integration of "people next door" perspectives Experience Cologne banner • Linking the musical with Cologne sights • Communicating the "Cologne experience" • Strong CTA for ticket booking Corporate events section • Presentation of business offers • Showcasing the possible combinations of business and pleasure • Presentation of VIP packages and special arrangements Quick links • Six attractively designed image tiles • Intuitive navigation to important subsections • Subject areas: Arrival & parking, ticket categories, performance times, corporate events, group offers, FAQ Footer area • Newsletter registration with emotional incentive • Clear contact information • Social media integration (Frendly, Pixaroo, Vidplex, Flipzy) • Area for legal information Functional requirements Responsive design • Optimal display on all devices (desktop, tablet, smartphone) • Special attention to mobile-first approach Performance • Fast loading times despite multimedia content • Optimization of all images and videos SEO optimization • SEO-friendly URL structure • Meta information for all pages • Semantic HTML structure • Keyword optimization for "Musical Cologne", "Comedy Musical", etc. • Special requirements for the wireframe Tonality and creativity The wireframe should already convey the cheeky, witty tone of the musical. Look for surprising elements that make you smile and capture the Cologne way of life. Integrate Cologne humor into UI elements, navigation terms, or micro-interactions. User path to ticket purchase Show how you can guide the user to ticket purchase through clever UX design. Pay particular attention to: • Strategic placement of calls to action • Reducing click paths to ticket purchases • Emotional triggers at decision points Surprising interaction elements Design unusual interaction elements that fit the character of the musical: • Cologne Cathedral that "sings" on hover • Interactive Cologne city scenes • Humorous loading animations • Easter eggs that appeal to Cologne insider knowledge Multi-device concept Show how your ideas work on different devices. Particularly important: • How navigation works on mobile devices • How complex elements like the seating plan are displayed on small screens • Which content is prioritized on mobile
Nice to have
• See briefing

```html
<!DOCTYPE html>
<html lang="en">
<head>
<meta charset="utf-8">
<title>Wolken und Brise – The Award-Winning Cologne Musical</title>
<link rel="stylesheet" href="https://fonts.googleapis.com/css2?family=Bebas+Neue&family=Open+Sans:wght@400;600;700&display=swap">
<style>
  :root {
    --ticker-purple: #a7269a;
    --magenta: #ad1b95;
    --plum: #72245f;
    --gold: #fbb72a;
    --white: #ffffff;
    --text-soft: #f3e6f0;
  }
  * { margin: 0; padding: 0; box-sizing: border-box; }
  html, body { width: 809px; height: 1200px; overflow: hidden; }
  body { position: relative; background: var(--plum); font-family: "Open Sans", sans-serif; color: var(--white); }

  .ticker {
    position: absolute; top: 0; left: 0; width: 809px; height: 27px;
    background: var(--ticker-purple); color: var(--gold);
    font-family: "Bebas Neue", sans-serif; font-size: 13.5px; line-height: 28px;
    text-align: center; white-space: nowrap;
  }

  .hero { position: absolute; top: 27px; left: 0; width: 809px; height: 477px; overflow: hidden; }
  .hero-visual {
    position: absolute; inset: 0;
    background:
      radial-gradient(ellipse 50% 45% at 55% 45%, rgba(120,95,80,.55), transparent 70%),
      radial-gradient(ellipse 30% 40% at 80% 55%, rgba(60,120,150,.35), transparent 70%),
      linear-gradient(180deg, #262220 0%, #3a322e 55%, #2a2321 100%);
  }
  .hero-shade { position: absolute; inset: 0; background: linear-gradient(90deg, rgba(0,0,0,.35), rgba(0,0,0,.1) 60%, rgba(0,0,0,.2)); }

  .brand {
    position: absolute; left: 101px; top: 36px; display: flex; align-items: center; gap: 5px;
    font-family: "Bebas Neue", sans-serif; font-size: 15px; line-height: 1; color: var(--gold);
    text-decoration: none; white-space: nowrap;
  }
  .brand-dot { width: 12px; height: 12px; border-radius: 50%; background: var(--gold); }

  .main-nav { position: absolute; top: 37px; left: 254px; display: flex; align-items: center; white-space: nowrap; }
  .main-nav a {
    font-family: "Bebas Neue", sans-serif; font-size: 13.5px; color: var(--white);
    text-decoration: none; margin-right: 13.5px; line-height: 20px; white-space: nowrap;
  }
  .main-nav a.is-active { color: var(--gold); }
  .main-nav a.nav-cta {
    background: var(--gold); color: var(--magenta); padding: 0 5px; height: 20px;
    margin: 0; min-width: 96px; text-align: center;
  }

  .hero-title {
    position: absolute; left: 101px; top: 194px;
    font-family: "Bebas Neue", sans-serif; font-weight: 400; font-size: 82px; line-height: 66px;
    color: #f4f4f4; letter-spacing: -1px;
  }
  .hero-subtitle { position: absolute; left: 101px; top: 320px; font-size: 25px; font-weight: 700; line-height: 32px; white-space: nowrap; }
  .hero-tagline { position: absolute; left: 101px; top: 350px; font-size: 14.5px; line-height: 18px; white-space: nowrap; }
  .hero-cta {
    position: absolute; left: 101px; top: 395px; width: 93px; height: 26px;
    background: var(--gold); color: var(--magenta); text-decoration: none;
    font-family: "Bebas Neue", sans-serif; font-size: 16px; line-height: 27px; text-align: center; white-space: nowrap;
  }
  .hero-price { position: absolute; left: 101px; top: 424px; font-size: 7px; white-space: nowrap; }
  .hero-price strong { font-weight: 600; }

  .endorsements { position: absolute; top: 504px; left: 0; width: 809px; height: 351px; background: var(--magenta); }
  .section-title { font-family: "Bebas Neue", sans-serif; font-weight: 400; text-align: center; color: var(--white); }
  .endorsements .section-title { position: absolute; top: 26px; width: 100%; font-size: 20px; line-height: 22px; }
  .celeb-card { position: absolute; top: 71px; width: 175px; height: 233px; overflow: hidden; }
  .celeb-photo {
    position: absolute; inset: 0;
    background: linear-gradient(180deg, #3b3437 0%, #5a4a52 50%, #8c3c8a 80%, #b226a0 100%);
  }
  .celeb-date {
    position: absolute; left: 13px; top: 10px;
    font-family: "Bebas Neue", sans-serif; font-size: 25px; line-height: 26px; color: var(--gold); letter-spacing: -.5px;
  }
  .celeb-name {
    position: absolute; left: 12px; bottom: 6px; font-weight: 400;
    font-family: "Bebas Neue", sans-serif; font-size: 25px; line-height: 20px; color: var(--white); letter-spacing: -.5px;
  }
  .slider-arrow {
    position: absolute; top: 178px; width: 18px; height: 18px; border-radius: 50%;
    background: var(--white); display: flex; align-items: center; justify-content: center;
  }

  .story { position: absolute; top: 855px; left: 0; width: 809px; height: 345px; background: var(--plum); overflow: hidden; }
  .skyline {
    position: absolute; left: 60px; right: 60px; bottom: 0; height: 200px;
    background: linear-gradient(180deg, rgba(150,50,140,0) 0%, rgba(150,50,140,.28) 50%, rgba(150,50,140,.35) 100%);
  }
  .story .section-title { position: absolute; top: 24px; width: 100%; font-size: 21px; line-height: 24px; white-space: nowrap; }
  .story-stats { position: absolute; top: 51px; width: 100%; text-align: center; font-size: 10.5px; line-height: 14px; color: var(--text-soft); }
  .story-text { position: absolute; top: 89px; width: 100%; text-align: center; font-size: 10.5px; line-height: 12.3px; color: var(--text-soft); white-space: nowrap; }
  .story-text strong { color: var(--white); font-weight: 700; }
  .experience-title { position: absolute; top: 160px; width: 100%; text-align: center; font-family: "Bebas Neue", sans-serif; font-weight: 400; font-size: 20px; color: var(--gold); line-height: 22px; }
  .highlights { position: absolute; top: 197px; width: 100%; list-style: none; text-align: center; }
  .highlights li {
    font-family: "Bebas Neue", sans-serif; font-size: 20px; line-height: 32.5px;
    letter-spacing: 2.4px; color: var(--gold); white-space: nowrap;
  }
</style>
</head>
<body>
  <div class="ticker">++ NEW: VIP PACKAGES NOW AVAILABLE ++ SPECIAL OFFER: 20% DISCOUNT FOR GROUPS OF 8 OR MORE ++ NEXT SHOW: [DATE] - SECURE THE BEST SEATS NOW! ++</div>

  <header class="hero">
    <div class="hero-visual" role="img" aria-label="Stage photo: cast members toasting with small glasses in a pub scene"></div>
    <div class="hero-shade"></div>

    <a class="brand" href="#"><span class="brand-dot"></span>Wolken und Brise</a>

    <nav class="main-nav">
      <a class="is-active" href="#">Musical</a>
      <a href="#">Ticket Info</a>
      <a href="#">Plan Your Visit</a>
      <a href="#">Groups</a>
      <a href="#">Corporate Events</a>
      <a href="#">FAQ</a>
      <a class="nav-cta" href="#">Secure Ticekts Now</a>
    </nav>

    <h1 class="hero-title">WOLKEN<br>UND BRISE</h1>
    <p class="hero-subtitle">The Award-Winning Cologne Musical</p>
    <p class="hero-tagline">A heavenly Cologne comedy that moves hearts and guarantees tears of laughter</p>
    <a class="hero-cta" href="#">Secure Ticekts</a>
    <p class="hero-price">Best seats starting at <strong>€44.90</strong></p>
  </header>

  <section class="endorsements">
    <h2 class="section-title">We are part of it too</h2>

    <article class="celeb-card" style="left:103px">
      <div class="celeb-photo" role="img" aria-label="Portrait of guest star Bernd Falkner"></div>
      <span class="celeb-date">17SEP</span>
      <h3 class="celeb-name">Bernd<br>Falkner</h3>
    </article>
    <article class="celeb-card" style="left:317px">
      <div class="celeb-photo" role="img" aria-label="Portrait of guest star Horst Wendelin"></div>
      <span class="celeb-date">18SEP</span>
      <h3 class="celeb-name">Horst<br>Wendelin</h3>
    </article>
    <article class="celeb-card" style="left:531px">
      <div class="celeb-photo" role="img" aria-label="Portrait of guest star Marco Lestani"></div>
      <span class="celeb-date">19SEP</span>
      <h3 class="celeb-name">Marco<br>Lestani</h3>
    </article>

    <span class="slider-arrow" style="left:94px" aria-label="Previous">
      <svg width="8" height="8" viewBox="0 0 8 8"><path d="M5.2 1 2.4 4l2.8 3" fill="none" stroke="#333" stroke-width="1.4"/></svg>
    </span>
    <span class="slider-arrow" style="left:697px" aria-label="Next">
      <svg width="8" height="8" viewBox="0 0 8 8"><path d="M2.8 1 5.6 4 2.8 7" fill="none" stroke="#333" stroke-width="1.4"/></svg>
    </span>
  </section>

  <section class="story">
    <div class="skyline" role="img" aria-label="Faint drawn Cologne skyline with cathedral and TV tower"></div>
    <h2 class="section-title">Germany’s first sustainable musical delights audiences and critics alike</h2>
    <p class="story-stats">4-time Award Winner &nbsp;|&nbsp; Over 140,000 Thrilled Visitors &nbsp;|&nbsp; 98% Recommendation Rate</p>
    <p class="story-text">Welcome to heavenly <strong>Cologne</strong>! Dive into a story only life could write:<br>Young pastor Gunnar leaves his quiet village parish and is transferred to the vibrant heart of Cologne.<br>What starts as a routine reassignment turns into a turbulent night full of surprises that changes his life forever.</p>
    <h3 class="experience-title">Experience:</h3>
    <ul class="highlights">
      <li>A top-class live orchestra</li>
      <li>Spectacular choreography</li>
      <li>Humor and depth in perfect harmony</li>
      <li>Captivating music ranging from jazz to Cologne pop</li>
    </ul>
  </section>
</body>
</html>
```